Dale Morrikan Plumbing and Heating

Need a card design for a plumbing and heating company that does service and repair, remodels, and plumbing in new construction. Please add following on back side of card; Boilers, Water heaters, Gas lines, Sump pumps, Toilet repairs, Faucet repairs, Pipe thawing, Radiant heating, New construction, Remodels.

Industry/Entity Type

Plumber

Contact Information for Business Card

Was thinking white gloss card with colored logo in middle or black glossy card with silver logo in middle. Just a thought but very open to other designs.

Requirements
Must have
• Need following on front of card;
• P(203) 321-8689
• C(203) 232-9069
• Dale Morrikan 275 Larkwell St West, Stamford, Ct 06214
• service@DrainHearth.example (plumbing in blue, heating in red)
• www.DrainHearth.example (plumbing in blue, heating in red)
• Fully Licensed and Insured
Nice to have
• Elegant design

```html
<!DOCTYPE html>
<html lang="en">
<head>
<meta charset="utf-8">
<title>Dale Morrikan Plumbing and Heating — Business Card</title>
<link rel="stylesheet" href="https://fonts.googleapis.com/css2?family=Saira:ital,wght@0,400;0,500;0,600;1,700&display=swap">
<style>
  :root {
    --backdrop: #3b3431;
    --card: #141414;
    --card-edge: #202020;
    --silver: #c9cdd3;
    --grey: #9a9ea4;
    --white: #f2f2f2;
    --blue: #2f5fd0;
    --red: #d42a2a;
    --divider: #8a8a8a;
  }
  html, body {
    margin: 0;
    width: 1200px;
    height: 780px;
    overflow: hidden;
    background: var(--backdrop);
    font-family: "Saira", sans-serif;
  }
  .canvas {
    width: 1200px;
    height: 780px;
    display: flex;
    align-items: center;
    justify-content: center;
    gap: 40px;
  }
  .card {
    width: 540px;
    height: 309px;
    background: var(--card);
    border: 1px solid var(--card-edge);
    border-radius: 4px;
    box-shadow: 0 14px 30px rgba(0,0,0,.45);
    position: relative;
    box-sizing: border-box;
    color: var(--white);
  }
  .brand {
    display: flex;
    align-items: center;
    gap: 10px;
  }
  .brand-dot {
    width: 22px;
    height: 22px;
    border-radius: 50%;
    background: var(--silver);
    flex: none;
  }
  .brand-name {
    font-weight: 600;
    color: var(--silver);
    text-transform: uppercase;
    letter-spacing: 1.5px;
    line-height: 1.15;
  }
  .brand-url {
    font-size: 11px;
    letter-spacing: .5px;
    margin-top: 3px;
  }
  .blue { color: var(--blue); }
  .red { color: var(--red); }

  /* back side */
  .card-back {
    display: flex;
    flex-direction: column;
    align-items: center;
    justify-content: center;
    gap: 26px;
  }
  .card-back .brand-name { font-size: 19px; text-align: center; }
  .service-list {
    margin: 0;
    text-align: center;
    font-size: 14px;
    line-height: 1.5;
    font-weight: 500;
  }

  /* front side */
  .card-front .brand {
    position: absolute;
    top: 62px;
    right: 36px;
  }
  .card-front .brand-name { font-size: 18px; text-align: right; }
  .card-front .brand-url { text-align: right; }
  .owner {
    position: absolute;
    left: 36px;
    top: 166px;
  }
  .owner-name {
    font-size: 21px;
    font-weight: 700;
    font-style: italic;
    color: var(--blue);
    margin: 0 0 6px;
  }
  .owner-address {
    font-size: 14px;
    line-height: 1.35;
    font-style: normal;
  }
  .contact {
    position: absolute;
    left: 232px;
    top: 196px;
    padding-left: 14px;
    border-left: 1px solid var(--divider);
    list-style: none;
    margin: 0;
    font-size: 13.5px;
    line-height: 1.55;
    font-weight: 500;
  }
  .contact li { display: flex; align-items: center; gap: 8px; }
  .icon {
    width: 14px;
    height: 14px;
    background: var(--red);
    border-radius: 2px;
    flex: none;
  }
</style>
</head>
<body>
<main class="canvas">

  <section class="card card-back" aria-label="Card back">
    <div class="brand">
      <span class="brand-dot" aria-hidden="true"></span>
      <div>
        <div class="brand-name">Dale Morrikan<br>Plumbing and Heating</div>
        <div class="brand-url"><span class="blue">www.Drain</span><span class="red">Hearth</span>.example</div>
      </div>
    </div>
    <p class="service-list">
      Boilers, Water heaters, Gas lines, Sump pumps, Toilet repairs<br>
      Faucet repairs, Pipe thawing, Radiant heating<br>
      New construction, Remodels
    </p>
  </section>

  <section class="card card-front" aria-label="Card front">
    <div class="brand">
      <span class="brand-dot" aria-hidden="true"></span>
      <div>
        <div class="brand-name">Dale Morrikan<br>Plumbing and Heating</div>
        <div class="brand-url"><span class="blue">www.Drain</span><span class="red">Hearth</span>.example</div>
      </div>
    </div>

    <div class="owner">
      <p class="owner-name">Dale Morrikan</p>
      <address class="owner-address">275 Larkwell St West<br>Stamford, Ct 06214</address>
    </div>

    <ul class="contact">
      <li>
        <svg class="icon" viewBox="0 0 14 14" aria-hidden="true"><rect width="14" height="14" rx="2" fill="#d42a2a"/><path d="M4 3.5c.6 2.9 3 5.6 6.5 6.5l.6-1.6-1.8-.8-.8.9c-1-.5-1.9-1.4-2.4-2.4l.9-.8-.8-1.8z" fill="#fff"/></svg>
        (203) 555-0147
      </li>
      <li>
        <svg class="icon" viewBox="0 0 14 14" aria-hidden="true"><rect width="14" height="14" rx="2" fill="#d42a2a"/><rect x="4.5" y="2.5" width="5" height="9" rx="1" fill="#fff"/><rect x="5.5" y="3.5" width="3" height="5.5" fill="#d42a2a"/></svg>
        (203) 555-0183
      </li>
      <li>
        <svg class="icon" viewBox="0 0 14 14" aria-hidden="true"><rect width="14" height="14" rx="2" fill="#d42a2a"/><rect x="2.5" y="4" width="9" height="6" fill="#fff"/><path d="M2.5 4l4.5 3.5L11.5 4" stroke="#d42a2a" fill="none"/></svg>
        service@<span class="blue">Drain</span><span class="red">Hearth</span>.example
      </li>
      <li>
        <svg class="icon" viewBox="0 0 14 14" aria-hidden="true"><rect width="14" height="14" rx="2" fill="#d42a2a"/><circle cx="7" cy="7" r="4" fill="none" stroke="#fff"/><path d="M3 7h8M7 3c-2 2.5-2 5.5 0 8M7 3c2 2.5 2 5.5 0 8" stroke="#fff" fill="none" stroke-width=".8"/></svg>
        www.<span class="blue">Drain</span><span class="red">Hearth</span>.example
      </li>
    </ul>
  </section>

</main>
</body>
</html>
```